Brookhaven Sound Vision Guard LLC

Need help designing a web page for an alarm company. I want to promote my business.

Target Market(s)

Residential and commercial clients

Industry/Entity Type

Security Service

Coding

Coded - Design and coding required

Number of Pages Required

2 page

Font styles to use
Sans Serif

Requirements
Must have
• I would llike my logo displayed on the page. I would like my slogan displayed as well
´´A GREAT PLACE FOR YOUR SECURITY NEEDS´´
We are licensed and insured
Company phone number 555-204-7163
Company hours: Monday-Friday 8am-5pm Company address: P.O. Box 412 Crosby, TX 77500 over 25 years experience
Email info. Brookhavensvg@mailbox.example
Company license #K41862259
Fire license# TDM-5817026
PLH-7064183
We offer alarm monitoring,security cameras, access control,gate openers, home theater systems, covert camera installations, FIre alarm installation and monitoring
Nice to have
• We offer security at competitive prices.
Get customer information for a free quote similar to vexo website.
Should not have
• No prices listed on website

```html
<!DOCTYPE html>
<html lang="en">
<head>
<meta charset="utf-8">
<title>Brookhaven Sound Vision Guard</title>
<link href="https://fonts.googleapis.com/css2?family=Audiowide&family=Hind:wght@300;400;500;600&family=Quicksand:wght@400;500&display=swap" rel="stylesheet">
<style>
:root{
  --red:#e31e2a;
  --red-dark:#c8141f;
  --ink:#222;
  --grey:#555a5e;
  --muted:#666;
  --pink:#fdf0f0;
  --footer:#262626;
  --white:#fff;
}
*{margin:0;padding:0;box-sizing:border-box}
html,body{width:1200px;height:3979px;overflow:hidden;background:var(--white)}
body{position:relative;font-family:'Hind',sans-serif;color:var(--ink)}
.abs{position:absolute}
.display{font-family:'Audiowide',sans-serif;text-transform:uppercase}
.shapes{position:absolute;left:0;top:0;width:1200px;height:3979px}

/* header */
.brand{left:170px;top:50px;width:220px;display:flex;align-items:center;gap:12px}
.brand .dot{width:40px;height:40px;border-radius:50%;background:var(--red);flex:none}
.brand span{font-family:'Hind',sans-serif;font-weight:600;color:var(--red);font-size:20px;line-height:1.05;text-transform:uppercase}
.contact-item{top:36px;display:flex;gap:10px;align-items:center}
.contact-item small{display:block;font-size:15px;line-height:1;color:var(--ink)}
.contact-item b{display:block;font-size:24px;font-weight:500;color:var(--red);line-height:1.2;white-space:nowrap}
.nav{top:130px;left:458px;width:569px;display:flex;justify-content:space-between;font-size:14.5px;font-weight:500;text-transform:uppercase}
.nav a{color:var(--ink);text-decoration:none}
.nav a.active{color:var(--red);position:relative}
.nav a.active::before{content:"";position:absolute;left:-8px;right:-8px;top:-9px;height:14px;border:2px solid var(--red);border-bottom:none;border-radius:50% 50% 0 0}

/* hero */
.hero-photo{left:0;top:175px;width:1200px;height:651px;background:linear-gradient(100deg,#6b6a6a 0%,#8f8c89 45%,#b4aea8 100%)}
.hero-title{left:170px;top:286px;font-size:41px;line-height:47px;color:var(--white);text-shadow:0 2px 4px rgba(0,0,0,.4)}
.quote{left:664px;top:259px;width:363px;height:369px;background:#eee;border-radius:10px;overflow:hidden}
.quote h2{background:var(--red);color:var(--white);font-size:27px;font-weight:500;text-align:center;height:75px;line-height:70px;border-radius:10px 10px 0 0}
.quote form{padding:24px 14px 0}
.field{display:block;height:47px;background:var(--white);border:1.5px solid #bbb;border-radius:7px;padding:0 9px;font-size:15px;line-height:45px;margin-bottom:13px}
.row{display:flex;gap:10px}.row .field{flex:1}
.btn{display:inline-block;background:var(--red);color:var(--white);border-radius:6px;font-size:15px;font-weight:500;padding:0 15px;height:46px;line-height:48px;text-transform:uppercase}

/* red band */
.band-name{left:0;width:1200px;top:846px;text-align:center;color:var(--white);font-weight:600;font-size:17px;text-transform:uppercase;letter-spacing:1px}
.band-title{left:0;width:1200px;top:903px;text-align:center;color:var(--white);font-size:31px}
.info{top:1197px;width:320px;text-align:center}
.info h3{font-weight:400;font-size:20px;text-transform:uppercase}
.info p{font-size:20px;font-weight:300}

/* about */
.eyebrow{font-size:21px;color:var(--ink)}
.section-title{color:var(--red);font-size:32px;line-height:36px}
.para{font-family:'Quicksand',sans-serif;font-size:12.5px;line-height:22.6px;color:#444}
.about-mark{left:633px;top:1359px;width:410px;height:254px;display:flex;align-items:center;justify-content:center;gap:16px}
.about-mark .dot{width:64px;height:64px;border-radius:50%;background:var(--red);flex:none}
.about-mark span{font-weight:600;color:var(--red);font-size:34px;line-height:1.05;text-transform:uppercase;width:300px}

/* services */
.services-title{left:0;width:1200px;top:1766px;text-align:center;color:var(--red);font-size:31px}
.card{width:246px;height:201px;background:var(--white);border:2px solid #bbb;text-align:center;padding-top:22px}
.card svg{width:46px;height:46px}
.card h4{font-weight:400;font-size:20px;text-transform:uppercase;margin-top:8px;line-height:1.2}
.card.hot h4{color:var(--red)}
.card p{font-family:'Quicksand',sans-serif;font-size:12.5px;line-height:20px;color:#555;padding:8px 14px 0}

/* fire */
.illus{left:108px;top:2517px;width:463px;height:340px;background:radial-gradient(ellipse at center,#d7d2cf 0%,#eceae9 55%,#fff 75%)}

/* smart home */
.smart-photo{left:0;top:2850px;width:1200px;height:640px;background:linear-gradient(90deg,#9a9a9a 0%,#c3c3c3 45%,#d9d6d3 100%)}
.smart-title{left:170px;top:3052px;font-size:43px;line-height:52px;color:var(--white)}
.smart-copy{left:170px;top:3162px;font-size:25px;line-height:39px;font-weight:300;color:var(--white);width:470px}

/* footer */
.foot-brand{left:170px;top:3640px;width:320px;display:flex;align-items:center;gap:16px}
.foot-brand .dot{width:58px;height:58px;border-radius:50%;background:var(--white);flex:none}
.foot-brand span{font-weight:600;color:var(--white);font-size:28px;line-height:1.05;text-transform:uppercase}
.foot-form{left:599px;top:3563px;width:428px}
.foot-form h3{color:var(--white);font-weight:300;font-size:26px;margin-bottom:26px}
.foot-form .field{border-radius:5px;height:47px;margin-bottom:12px}
.foot-form .msg{height:86px;line-height:30px}
.rule{left:170px;top:3891px;width:857px;height:1px;background:#888}
.copy{left:0;width:1200px;top:3925px;text-align:center;color:var(--white);font-size:13px}
</style>
</head>
<body>

<svg class="shapes" viewBox="0 0 1200 3979" aria-hidden="true">
  <path d="M0 1775 Q600 1621 1200 1775 L1200 2332 Q600 2486 0 2332 Z" fill="var(--pink)"/>
</svg>

<!-- header -->
<div class="abs brand"><i class="dot"></i><span>Brookhaven Sound Vision Guard</span></div>
<div class="abs contact-item" style="left:548px">
  <svg width="26" height="50" viewBox="0 0 26 50"><rect x="2" y="2" width="22" height="46" rx="4" fill="none" stroke="var(--red)" stroke-width="3"/><rect x="6" y="9" width="14" height="28" fill="var(--red)"/></svg>
  <div><small>PHONE NUMBER</small><b>555-204-7163</b></div>
</div>
<div class="abs contact-item" style="left:749px">
  <svg width="28" height="50" viewBox="0 0 28 50"><rect x="2" y="2" width="24" height="46" rx="4" fill="none" stroke="var(--red)" stroke-width="3"/><path d="M7 16h14v12H7zM7 16l7 7 7-7" fill="none" stroke="var(--red)" stroke-width="2"/></svg>
  <div><small>EMAIL INFO</small><b style="font-size:18.5px">Brookhavensvg@mailbox.example</b></div>
</div>
<nav class="abs nav"><a class="active">Home</a><a>Packages</a><a>Services &amp; Solutions</a><a>Products</a><a>Why Us</a><a>Contact</a></nav>

<!-- hero -->
<div class="abs hero-photo" role="img" aria-label="Photo of a hand holding a smartphone running a smart home security app in a bright living room"></div>
<h1 class="abs hero-title display">A Great Place<br>for your Security<br>Needs</h1>
<div class="abs quote">
  <h2>GET A FREE QUOTE</h2>
  <form>
    <span class="field">Name</span>
    <span class="field">Email</span>
    <div class="row"><span class="field">Phone</span><span class="field">Zip</span></div>
    <span class="btn" style="height:46px;font-size:14px">Get a free quote</span>
  </form>
</div>

<!-- red band -->
<svg class="shapes" viewBox="0 0 1200 3979" aria-hidden="true">
  <path d="M0 826 Q600 702 1200 826 L1200 1086 L0 1086 Z" fill="var(--red)"/>
  <g id="circ">
    <path d="M190 1088 A96 96 0 0 1 382 1088 Z" fill="#fff"/>
    <path d="M190 1088 A96 96 0 0 0 382 1088 Z" fill="var(--grey)"/>
    <circle cx="286" cy="1088" r="66" fill="var(--red)"/>
    <circle cx="286" cy="1088" r="50" fill="var(--grey)"/>
  </g>
  <use href="#circ" x="313"/>
  <use href="#circ" x="613"/>
  <circle cx="286" cy="1088" r="24" fill="none" stroke="#fff" stroke-width="3"/>
  <path d="M286 1074v14l9 6" fill="none" stroke="#fff" stroke-width="3"/>
  <path d="M599 1116c-14-16-20-26-20-34a20 20 0 0 1 40 0c0 8-6 18-20 34z" fill="none" stroke="#fff" stroke-width="3"/>
  <circle cx="599" cy="1082" r="7" fill="none" stroke="#fff" stroke-width="3"/>
  <rect x="873" y="1071" width="52" height="34" fill="none" stroke="#fff" stroke-width="3"/>
  <path d="M873 1071l26 20 26-20M873 1105l19-17M925 1105l-19-17" fill="none" stroke="#fff" stroke-width="3"/>
</svg>
<div class="abs band-name">Brookhaven Sound Vision Guard</div>
<h2 class="abs band-title display">Customize your alarm system today</h2>
<div class="abs info" style="left:126px"><h3>Company Hours</h3><p>Monday-Friday 8am-5pm</p></div>
<div class="abs info" style="left:439px"><h3>Company Address</h3><p>P.O. Box 412 Crosby, TX 77500</p></div>
<div class="abs info" style="left:739px"><h3>Email Info</h3><p style="font-size:18px">Brookhavensvg@mailbox.example</p></div>

<!-- about -->
<div class="abs" style="left:170px;top:1356px;width:440px">
  <div class="eyebrow display">About</div>
  <h2 class="section-title display">Brookhaven Sound Vision Guard</h2>
  <p class="para" style="margin-top:22px">We are licensed and insured, with over 25 years experience protecting residential and commercial clients. We offer security at competitive prices, from alarm monitoring and security cameras to access control, gate openers and covert camera installations. Company License #K41862259. Fire License #TDM-5817026. License #PLH-7064183. Ask us today for a free quote.</p>
</div>
<div class="abs about-mark"><i class="dot"></i><span>Brookhaven Sound Vision Guard</span></div>

<!-- services -->
<h2 class="abs services-title display">Our Services</h2>
<div class="abs card" style="left:202px;top:1848px">
  <svg viewBox="0 0 46 46"><path d="M8 10h30l-4 8H12z" fill="none" stroke="#222" stroke-width="3"/><circle cx="23" cy="28" r="10" fill="none" stroke="#222" stroke-width="3"/><circle cx="23" cy="28" r="4" fill="#222"/></svg>
  <h4>Alarm Monitoring</h4><p>At vero eos et accusamus et iusto odio dignissimos ducimus qui blan ditiis praesentium.</p></div>
<div class="abs card hot" style="left:477px;top:1848px">
  <svg viewBox="0 0 46 46"><rect x="14" y="10" width="26" height="13" rx="2" fill="none" stroke="var(--red)" stroke-width="3"/><path d="M40 13l5-3v10l-5-3M20 23v8H8M8 26v10" fill="none" stroke="var(--red)" stroke-width="3"/></svg>
  <h4>Security Cameras</h4><p>At vero eos et accusamus et iusto odio dignissimos ducimus qui blan ditiis praesentium.</p></div>
<div class="abs card" style="left:752px;top:1848px">
  <svg viewBox="0 0 46 46"><path d="M23 4l15 6v11c0 10-7 17-15 21C15 38 8 31 8 21V10z" fill="none" stroke="#222" stroke-width="3"/><path d="M16 23l5 5 9-10" fill="none" stroke="#222" stroke-width="3"/></svg>
  <h4>Access Control</h4><p>At vero eos et accusamus et iusto odio dignissimos ducimus qui blan ditiis praesentium.</p></div>
<div class="abs card hot" style="left:202px;top:2080px">
  <svg viewBox="0 0 46 46"><path d="M8 20L26 6l16 14M12 17v15h12M38 17v15" fill="none" stroke="var(--red)" stroke-width="3"/><circle cx="10" cy="38" r="5" fill="none" stroke="var(--red)" stroke-width="3"/><path d="M15 38h16v4" fill="none" stroke="var(--red)" stroke-width="3"/><path d="M21 18l4 4 7-7" fill="none" stroke="var(--red)" stroke-width="3"/></svg>
  <h4>Gate Openers</h4><p>At vero eos et accusamus et iusto odio dignissimos ducimus qui blan ditiis praesentium.</p></div>
<div class="abs card" style="left:477px;top:2080px">
  <svg viewBox="0 0 46 46"><rect x="4" y="6" width="8" height="30" fill="none" stroke="#222" stroke-width="3"/><rect x="34" y="6" width="8" height="30" fill="none" stroke="#222" stroke-width="3"/><rect x="15" y="8" width="16" height="12" fill="none" stroke="#222" stroke-width="3"/><path d="M15 26h16M4 40h38" stroke="#222" stroke-width="3"/></svg>
  <h4>Home Theater Systems</h4><p>At vero eos et accusamus et iusto odio dignissimos ducimus qui blan ditiis praesentium.</p></div>
<div class="abs card hot" style="left:752px;top:2080px">
  <svg viewBox="0 0 46 46"><path d="M6 10h34M10 10v6a13 13 0 0 0 26 0v-6" fill="none" stroke="var(--red)" stroke-width="3"/><circle cx="23" cy="19" r="6" fill="none" stroke="var(--red)" stroke-width="3"/><circle cx="23" cy="19" r="2" fill="var(--red)"/></svg>
  <h4>Camera Installations</h4><p>At vero eos et accusamus et iusto odio dignissimos ducimus qui blan ditiis praesentium.</p></div>

<!-- fire -->
<div class="abs illus" role="img" aria-label="Isometric illustration of a house connected to security cameras, sensors, a control panel and monitoring devices"></div>
<div class="abs" style="left:598px;top:2526px;width:430px">
  <div class="eyebrow display">Fire</div>
  <h2 class="section-title display">Alarm Installation and Monitoring</h2>
  <p class="para" style="margin-top:22px">Nam libero tempore, cum soluta nobis est eligendi optio cumque nihil impedit quo minus id quod maxime placeat facere possimus, omnis voluptas assumenda est, omnis dolor repellendus. Temporibus autem quibusdam et aut officiis debitis aut rerum necessitatibus saepe eveniet ut et voluptates repudiandae sint et molestiae non recusandae. Itaque earum rerum hic tenetur.</p>
  <span class="btn display" style="margin-top:26px;font-size:13px;height:46px;line-height:46px">Read More</span>
</div>

<!-- smart home -->
<div class="abs smart-photo" role="img" aria-label="Photo of a smiling family sitting under a white roof shape against a light brick wall"></div>
<svg class="shapes" viewBox="0 0 1200 3979" aria-hidden="true">
  <path d="M0 2850 L1200 2850 L1200 2995 Q600 2857 0 2995 Z" fill="#fff"/>
  <path d="M0 3405 Q600 3559 1200 3405 L1200 3979 L0 3979 Z" fill="var(--footer)"/>
</svg>
<h2 class="abs smart-title display">Smarter Home<br>Security</h2>
<p class="abs smart-copy">Get best-in-class security, plus smart home automation the whole family will love.</p>
<span class="abs btn display" style="left:170px;top:3272px;font-size:13px;height:46px;line-height:46px">Read More</span>

<!-- footer -->
<div class="abs foot-brand"><i class="dot"></i><span>Brookhaven Sound Vision Guard</span></div>
<div class="abs foot-form">
  <h3>Contact Form</h3>
  <div class="row"><span class="field">Name</span><span class="field">Email</span></div>
  <span class="field msg">Message</span>
  <span class="btn" style="margin-top:6px">Submit Now</span>
</div>
<div class="abs rule"></div>
<div class="abs copy">Copyrights @ 2020 Brookhaven Sound Vision Guard. All Rights Reserved.</div>

</body>
</html>
```